Letterhead to Introduce a 'Sister' Company.

What I am needing is a design for a letter head to introduce our current customers base of (KT Alarm) customers to our new service, 'Kestrel Tide Solar Brokers'

```html
<!DOCTYPE html>
<html lang="en">
<head>
<meta charset="utf-8">
<title>KT Alarm &amp; Kestrel Tide Solar Brokers – Letterhead</title>
<link href="https://fonts.googleapis.com/css2?family=Asap+Condensed:wght@400&family=Montserrat:wght@300;400;600;700&display=swap" rel="stylesheet">
<style>
  :root {
    --brand-blue: #00579a;
    --brand-green: #4db848;
    --ink: #555759;
    --ink-dark: #58595b;
    --paper: #ffffff;
    --backdrop: #d6d6d6;
  }
  * { margin: 0; padding: 0; box-sizing: border-box; }
  html, body { width: 1056px; height: 1200px; overflow: hidden; background: var(--backdrop); }
  .canvas { position: relative; width: 1056px; height: 1200px; }
  .letterhead {
    position: absolute; left: 104px; top: 0;
    width: 1065px; height: 1507px;
    transform: scale(0.7962); transform-origin: 0 0;
    background: var(--paper);
    overflow: hidden;
    font-family: "Montserrat", sans-serif;
    color: var(--ink);
  }
  .edge-band { position: absolute; left: 0; width: 100%; }
  .edge-band-top { top: 0; height: 26px; background: var(--brand-blue); border-bottom: 8px solid var(--brand-green); }
  .edge-band-bottom { bottom: 0; height: 26px; background: var(--brand-blue); border-top: 8px solid var(--brand-green); }
  .brand-name {
    position: absolute; font-family: "Montserrat", sans-serif; font-weight: 700;
    color: var(--brand-blue); letter-spacing: 0.5px; line-height: 1;
  }
  .brand-alarm { left: 226px; top: 134px; font-size: 46px; }
  .brand-solar { left: 700px; top: 118px; width: 265px; text-align: center; font-size: 30px; line-height: 1.15; }
  .letter-body { position: absolute; left: 100px; top: 438px; width: 865px; }
  .date { font-size: 23px; font-weight: 300; color: var(--ink); }
  .recipient-name { margin-top: 14px; font-size: 38px; font-weight: 700; color: var(--ink-dark); letter-spacing: 0.3px; }
  .recipient-title { margin-top: 4px; font-size: 23px; font-weight: 300; }
  .message { margin-top: 60px; font-family: "Asap Condensed", sans-serif; font-size: 22.5px; line-height: 37px; text-align: justify; color: var(--ink); }
  .message p + p { margin-top: 37px; }
  .closing { margin-top: 70px; font-family: "Asap Condensed", sans-serif; font-size: 24px; }
  .signature { margin-top: 20px; width: 112px; height: 76px; background: linear-gradient(135deg, #e6eef6, #cfdcea); border-radius: 4px; }
  .contact { position: absolute; left: 100px; top: 1306px; font-size: 18px; font-weight: 400; color: var(--ink-dark); }
  .contact-address { line-height: 23px; }
  .contact-list { list-style: none; margin-top: 12px; }
  .contact-list li { display: flex; align-items: center; height: 25.5px; }
  .contact-list svg { width: 18px; height: 18px; margin-right: 17px; fill: none; stroke: var(--brand-blue); stroke-width: 1.6; }
</style>
</head>
<body>
<div class="canvas">
  <div class="letterhead">
    <div class="edge-band edge-band-top" aria-hidden="true"></div>

    <div class="brand-name brand-alarm">KT Alarm</div>
    <div class="brand-name brand-solar">Kestrel Tide<br>Solar Brokers</div>

    <main class="letter-body">
      <p class="date">10 December, 2021</p>
      <h1 class="recipient-name">DANIEL REYES</h1>
      <p class="recipient-title">Cheif Executive Officer</p>

      <div class="message">
        <p>Contrary to popular belief, Lorem Ipsum is not simply random text. It has roots in a piece of classical Latin literature from 45 BC, making it over 2000 years old. Henry Aldous, a Latin professor at Ashford College in Virginia, looked up one of the more obscure Latin words, consectetur.</p>
        <p>Lorem Ipsum comes from sections 1.10.32 and 1.10.33 of "de Finibus Bonorum et Malorum" (The Extremes of Good and Evil) by Cicero, written in 45 BC. This book is a treatise on the theory of ethics, very popular during the Renaissance. The first line of Lorem Ipsum.</p>
        <p>The standard chunk of Lorem Ipsum used since the 1500s is reproduced below for those interested.</p>
      </div>

      <p class="closing">Best Regards</p>
      <div class="signature" role="img" aria-label="Handwritten signature of the sender"></div>
    </main>

    <footer class="contact">
      <p class="contact-address">PO Box 2271. Port Avery,<br>WA 98412</p>
      <ul class="contact-list">
        <li><svg viewBox="0 0 20 20"><path d="M4 2 L7 2 L8.5 6 L6.5 7.5 C7.5 10 10 12.5 12.5 13.5 L14 11.5 L18 13 L18 16 C18 17 17 18 16 18 C8.5 17.5 2.5 11.5 2 4 C2 3 3 2 4 2 Z"/></svg>888-555-0142</li>
        <li><svg viewBox="0 0 20 20"><rect x="1.5" y="4" width="17" height="12"/><path d="M1.5 4 L10 11 L18.5 4"/></svg>info@kthomesecurity.com</li>
        <li><svg viewBox="0 0 20 20"><circle cx="10" cy="10" r="8"/><ellipse cx="10" cy="10" rx="3.5" ry="8"/><path d="M2 10 H18 M3.5 6 H16.5 M3.5 14 H16.5"/></svg>www.kthomesecurity.com</li>
      </ul>
    </footer>

    <div class="edge-band edge-band-bottom" aria-hidden="true"></div>
  </div>
</div>
</body>
</html>
```